PREMIUM AGENCY High End Business Card - A+++ Designers Wanted

** DO NOT ATTEMPT TO CONTACT ME THROUGH SEARCHING ON ZINTREL OR EMAILING ME THROUGH MY WEBSITE **

I need a fresh, contemporary business card designed using the logo attached (BRONSALK)

I have attached the font for BRONSALK

It must have a premium look and feel. The business card size must be STANDARD size.

You can submit either/both VERTICAL or HORIZONTAL designs.

FRONT: It must have the following sample information on

Paul Ardley
Director Operations
Mobile +61 452 118 906
Email paulardley@bronsalk.com
www.bronsalk.com

The REAR of the business card must have the words

CREATE INSPIRE TOMORROW

as part of the design, in the same font (NEXA) attached.

The words do not need to be in capitals, or on the same line, please design this as you see it best working.

ADDITIONAL INFORMATION
======================

The BRONSALK logo must be on the front of the card

I want Ultraviolet printing on the final design, to enhance either the NAME of the person OR the BRONSALK logo OR the words on the back of the card.

Target Market(s)

Agency, Advertising Agency, Creative, Designers

Industry/Entity Type

Media

Contact Information for Business Card

Design Agency, Contemporary, Premium look and feel, High Quality

Font styles to use
Serif
Sans Serif
Other font styles liked:
• ATTACHED TO PROJECT

Requirements
Must have
• BLACK & WHITE as the primary design, and if you feel there can be a highlighted colour, then this can be used.
• The Logo ICON attached is blue, this colour must not be changed.
• I have attached the partner brand BRONSALK MEDIA incase you need to manipulate the original files.
• ** DO NOT ATTEMPT TO CONTACT ME THROUGH SEARCHING ON ZINTREL OR EMAILING ME THROUGH MY WEBSITE **
Nice to have
• Must be Premium. I have attached some sample designs, that I like that would be a good inspiration for where this can be taken.
• My favourite design is is the KESTRAVUE2-BUSINESSCARD-TEMPLATE
Should not have
• No funny or silly standard / off the shelf designs

```html
<!DOCTYPE html>
<html lang="en">
<head>
<meta charset="utf-8">
<title>Bronsalk Business Card</title>
<link rel="stylesheet" href="https://fonts.googleapis.com/css2?family=Raleway:wght@200;300;400;500&display=swap">
<style>
  :root {
    --backdrop: #d9d9da;
    --card: #1b1c1e;
    --brand-blue: #35a9e1;
    --text-light: #c9cbcd;
    --text-mid: #8d9094;
  }
  * { margin: 0; padding: 0; box-sizing: border-box; }
  html, body {
    width: 1200px;
    height: 901px;
    overflow: hidden;
    background: var(--backdrop);
  }
  .stage {
    width: 1200px;
    height: 901px;
    display: flex;
    align-items: center;
    justify-content: center;
  }
  .card {
    position: relative;
    width: 470px;
    height: 822px;
    background: var(--card);
    border-radius: 6px;
    overflow: hidden;
    font-family: "Raleway", "Helvetica Neue", Arial, sans-serif;
  }
  .contact-block {
    position: absolute;
    top: 78px;
    left: 0;
    right: 0;
    text-align: center;
  }
  .person-name {
    color: var(--brand-blue);
    font-weight: 200;
    font-size: 54px;
    line-height: 1.02;
    letter-spacing: 1px;
    text-transform: uppercase;
  }
  .person-role {
    margin-top: 16px;
    color: var(--text-mid);
    font-weight: 300;
    font-size: 17px;
    letter-spacing: 1.5px;
    text-transform: uppercase;
  }
  .person-details {
    margin-top: 26px;
    list-style: none;
    color: var(--text-light);
    font-weight: 500;
    font-size: 17px;
    line-height: 1.5;
    letter-spacing: 1.2px;
    text-transform: uppercase;
  }
  .brand-mark {
    position: absolute;
    left: 0;
    bottom: 130px;
    display: flex;
    align-items: center;
    gap: 16px;
    padding-left: 40px;
  }
  .brand-dot {
    width: 22px;
    height: 22px;
    border-radius: 50%;
    background: var(--brand-blue);
  }
  .brand-name {
    color: var(--brand-blue);
    font-weight: 300;
    font-size: 58px;
    letter-spacing: 3px;
  }
  .website {
    position: absolute;
    right: 40px;
    bottom: 48px;
    color: var(--text-light);
    font-weight: 400;
    font-size: 18px;
    letter-spacing: 1.5px;
    text-transform: uppercase;
  }
  .website strong {
    color: var(--brand-blue);
    font-weight: 400;
  }
</style>
</head>
<body>
<main class="stage">
  <article class="card">
    <section class="contact-block">
      <h1 class="person-name">Paul<br>Ardley</h1>
      <p class="person-role">Director Operations</p>
      <ul class="person-details">
        <li>p.ardley@bronsalk.com</li>
        <li>+61 452 118 906</li>
      </ul>
    </section>
    <div class="brand-mark">
      <span class="brand-dot"></span>
      <span class="brand-name">BRONSALK</span>
    </div>
    <p class="website">www.<strong>bronsalk</strong>.com</p>
  </article>
</main>
</body>
</html>
```